Visitenkartenerstellung für Dorvek-Estates
Zielgruppe
Männer und Frauen, junge Familien bis hin zum Senior.
Verkauf von hochwertigen Immobilien in Spanien.
Aufgabenstellung
Auf Grund unserer Namensänderung benötigen wir ein neues Visitenkartendesign.
Wir sind eine skandinavische Agentur für Luxus-Immobilien auf Mallorca.
Das Design sollte dementsprechend edel aber dennoch schlicht gestaltet sein!

```html
<!DOCTYPE html>
<html lang="de">
<head>
<meta charset="utf-8">
<title>Dorvek-Estates – Visitenkarte</title>
<link rel="stylesheet" href="https://fonts.googleapis.com/css2?family=Lato:wght@300;400;700&display=swap">
<style>
  :root {
    --page-bg: #f1f1f1;
    --card-dark: #282425;
    --card-light: #ffffff;
    --card-edge: #8a8a8a;
    --text-light: #ffffff;
    --text-soft: #e6e6e6;
    --text-dark: #1f1c1d;
    --text-body: #4a4a4a;
  }
  html, body {
    margin: 0;
    padding: 0;
    width: 1200px;
    height: 754px;
    overflow: hidden;
    background: var(--page-bg);
    font-family: "Lato", sans-serif;
  }
  .stage {
    position: relative;
    width: 1200px;
    height: 754px;
  }
  .card {
    position: absolute;
    box-sizing: border-box;
  }
  .card-front {
    left: 177px;
    top: 92px;
    width: 485px;
    height: 313px;
    background: var(--card-dark);
  }
  .card-back {
    left: 564px;
    top: 354px;
    width: 483px;
    height: 312px;
    background: var(--card-light);
    border: 1px solid var(--card-edge);
  }
  .company-name {
    position: absolute;
    left: 78px;
    top: 108px;
    margin: 0;
    font-weight: 300;
    font-size: 46px;
    line-height: 1;
    color: var(--text-light);
    white-space: nowrap;
  }
  .tagline {
    position: absolute;
    left: 78px;
    top: 183px;
    margin: 0;
    font-weight: 300;
    font-size: 17.5px;
    color: var(--text-soft);
    white-space: nowrap;
  }
  .person-name {
    position: absolute;
    left: 40px;
    top: 75px;
    margin: 0;
    font-weight: 700;
    font-size: 20.5px;
    letter-spacing: 0.4px;
    color: var(--text-dark);
  }
  .person-role {
    position: absolute;
    left: 40px;
    top: 102px;
    margin: 0;
    font-weight: 300;
    font-size: 16.5px;
    color: var(--text-body);
  }
  .contact-block {
    position: absolute;
    left: 277px;
    top: 101px;
    margin: 0;
    font-style: normal;
    font-weight: 300;
    font-size: 16.5px;
    line-height: 24.5px;
    color: var(--text-body);
    white-space: nowrap;
  }
  .contact-line {
    display: block;
  }
  .contact-footer {
    position: absolute;
    left: 40px;
    top: 237px;
    margin: 0;
    font-weight: 300;
    font-size: 16px;
    color: var(--text-body);
    white-space: nowrap;
  }
</style>
</head>
<body>
<main class="stage">
  <section class="card card-front" aria-label="Vorderseite">
    <h1 class="company-name">Dorvek-Estates</h1>
    <p class="tagline">Luxury Real Estate on Mallorca &amp; Ibiza</p>
  </section>

  <section class="card card-back" aria-label="Rückseite">
    <h2 class="person-name">LINNEA HALLBERG</h2>
    <p class="person-role">Property Manager</p>
    <address class="contact-block">
      <span class="contact-line">C. Miramar 8</span>
      <span class="contact-line">&nbsp;07181 Calvià Spain</span>
      <span class="contact-line">Tel. 971584206</span>
      <span class="contact-line">Mobil 0034 61583947</span>
    </address>
    <p class="contact-footer">Linnea.Hallberg@dorvek-estates.com · www.dorvek-estates.se</p>
  </section>
</main>
</body>
</html>
```